We are launching in December, a range of supplements and vitamins.

We have just made an amend to the mission statement and how we are going to give back to society. Please can you add both to the packaging:

Verdane’s purpose is to support health, wellbeing and longevity, so that we can all thrive in the modern world; an environment so alien to that in which we evolved. Embracing technology, research and science, we harness nature’s goodness - enabling us all to love life – naturally.

Twice Each Day Pledge. For each and every Verdane supplement you take, we provide a supplement to an under nourished child.

For every supplement we sell: £1 goes to the charity ‘Little Lanterns Fund’ and in addition we provide one healthy meal to an under privileged child in India.

My name is Mark Holloway and I own several companies including www.lustrova.com (you can check me out on Infopedon – I am not the football referee nor the rocket scientist, but the entrepreneur) . Over the past 2 years I have been writing a book to help people live more healthily and it launches in December. It’s called Verdane Way. While doing my research for the book, I came to realise that most supplements and vitamin products on the market are rubbish! Most are made for profit and not for the benefit of the consumer. I want to change all of that. Gordon Ashby is patron of a charity I set up with my brother Paul Holloway and together we have built 11 schools in Asia. I am hoping to get Gordons help in getting my supplements to market.

Positioning of our supplements - In a world where so much has changed from the one our bodies were designed to thrive, at Verdane Supplements we are driven by one purpose; to globally provide healthy support to life in the 21st century. While the roots of our wellbeing supplements date back beyond 10,000BC, we embrace modern technology and science, to encapsulate powerful phytonutrients, herbs and other goodness. The essence of which is to promote health, happiness and longevity.

So what are we looking for in the design? Something that stands out. Something that looks professional. A design and concept that can role out across 24 different products. Some products are simple, just one ingredient, such as vitamin D3, Magnesium, Garlic Extracts etc, and others are our own formulas where there are up to 30 different ingredients. You can contact me at any time with questions at Mark@verdaneway.com

Target Market(s)

Male & Female 20 years plus, mainly UK

Industry/Entity Type

Medical

Logo Text

VERDANE - Sub heading = Thriving Days Outdoors

Colors

Designer to choose colors to be used in the design.

Requirements
Must have
• see attached powerpoint.
• We have just made an amend to the mission statement and how we are going to give back to society. Please can you add both to the packaging:
• Verdane’s purpose is to support health, wellbeing and longevity, so that we can all thrive in the modern world; an environment so alien to that in which we evolved. Embracing technology, research and science, we harness nature’s goodness - enabling us all to love life – naturally.
• Twice Each Day Pledge. For each and every Verdane supplement you take, we provide a supplement to an under nourished child.
Nice to have
• see attached powerpoint
Should not have
• see attached powerpoint

```html
<!DOCTYPE html>
<html lang="en">
<head>
<meta charset="utf-8">
<title>Verdane Way – Supplement Labels</title>
<link rel="stylesheet" href="https://fonts.googleapis.com/css2?family=Oswald:wght@300;400;500;600;700&family=Roboto+Slab:wght@700&family=Playfair+Display:ital@1&family=Josefin+Sans:wght@300;400&family=Courier+Prime:wght@700&display=swap">
<style>
  :root{
    --page:#efefef;
    --paper:#ffffff;
    --ink:#111111;
    --cream:#f4f1ea;
    --seal:#c9ab6e;
    --seal-ring:#a88a4e;

    --sleep-deep:#12284a;  --sleep-mid:#1d4f9a;  --sleep-logo:#1b6fd0;
    --tea-deep:#12402a;    --tea-mid:#1f7a4a;    --tea-logo:#2bb673;
    --energy-deep:#4a0f16; --energy-mid:#9c1b26; --energy-logo:#d3202e;
    --d3-deep:#4a3210;     --d3-mid:#c08419;     --d3-logo:#d4900f;
  }
  *{box-sizing:border-box;margin:0;padding:0}
  html,body{width:1200px;height:900px;overflow:hidden}
  body{background:var(--page);position:relative;font-family:"Oswald",sans-serif}

  .label{
    position:absolute;width:521px;height:316px;background:var(--paper);overflow:hidden;
  }
  .label--sleep{left:56px;top:101px;--deep:var(--sleep-deep);--mid:var(--sleep-mid);--logo:var(--sleep-logo)}
  .label--tea{left:622px;top:101px;--deep:var(--tea-deep);--mid:var(--tea-mid);--logo:var(--tea-logo)}
  .label--energy{left:56px;top:483px;--deep:var(--energy-deep);--mid:var(--energy-mid);--logo:var(--energy-logo)}
  .label--d3{left:622px;top:483px;--deep:var(--d3-deep);--mid:var(--d3-mid);--logo:var(--d3-logo)}

  .label__art{
    position:absolute;left:0;top:0;width:352px;height:316px;
    background:
      radial-gradient(ellipse at 65% 40%, var(--mid) 0%, transparent 60%),
      radial-gradient(ellipse at 20% 80%, var(--mid) 0%, transparent 55%),
      linear-gradient(135deg, var(--deep) 0%, var(--mid) 55%, var(--deep) 100%);
    clip-path:polygon(0 0,341px 0,347px 12px,338px 26px,348px 41px,340px 57px,350px 74px,339px 90px,346px 106px,337px 124px,349px 140px,340px 158px,347px 175px,336px 192px,348px 209px,339px 226px,350px 243px,340px 260px,347px 277px,337px 294px,345px 308px,341px 316px,0 316px);
  }

  .label__seal{
    position:absolute;left:22px;top:-36px;width:112px;height:112px;border-radius:50%;
    background:var(--seal);border:4px solid var(--seal-ring);box-shadow:inset 0 0 0 6px var(--seal);
  }

  .label__info{position:absolute;left:38px;top:0;width:272px;color:var(--cream)}
  .est-line{
    position:absolute;top:66px;left:-8px;width:290px;display:flex;align-items:baseline;
    font-family:"Josefin Sans",sans-serif;
  }
  .est-line__est{font-size:10px;letter-spacing:5px}
  .est-line__name{font-size:20px;font-weight:300;letter-spacing:5px;margin-left:22px}
  .est-line__year{font-family:"Oswald",sans-serif;font-size:10px;font-weight:500;margin-left:auto}

  .label__title{
    position:absolute;top:92px;left:-8px;width:290px;text-align:center;
    font-family:"Oswald",sans-serif;font-weight:600;font-size:50px;line-height:1;letter-spacing:3px;
  }
  .label__title sup{font-size:26px;vertical-align:top;position:relative;top:-4px}

  .dose{
    position:absolute;top:158px;left:-4px;width:286px;display:flex;align-items:center;
  }
  .dose__pill{width:22px;height:14px}
  .dose__count{font-family:"Playfair Display",serif;font-size:15px;margin-left:2px}
  .dose__kind{font-family:"Roboto Slab",serif;font-weight:700;font-size:15px;letter-spacing:2px;margin-left:16px}
  .dose__kind--wide{letter-spacing:5px}
  .dose__mg{font-family:"Playfair Display",serif;font-style:italic;font-size:14px;margin-left:auto}

  .rule{position:absolute;left:-6px;width:284px;height:2px;background:var(--cream);border-radius:2px}
  .rule--1{top:186px}.rule--2{top:254px}.rule--3{top:292px}

  .copy{position:absolute;left:0;width:272px;font-weight:300;font-size:10.2px;line-height:13.4px}
  .copy strong{font-weight:600}
  .copy--purpose{top:196px}
  .copy--pledge{top:263px}

  .label__brand{position:absolute;left:352px;top:0;width:169px;height:316px;text-align:center}
  .brand-name{
    position:absolute;top:62px;left:0;width:169px;
    font-family:"Oswald",sans-serif;font-weight:700;font-size:40px;line-height:38px;color:var(--logo);letter-spacing:1px;
  }
  .brand-tagline{
    position:absolute;top:140px;left:12px;width:145px;padding:1px 0;
    font-family:"Courier Prime",monospace;font-weight:700;font-size:9px;color:var(--ink);
    border-top:1.5px solid var(--ink);border-bottom:1.5px solid var(--ink);
  }
  .natural-badge{position:absolute;left:38px;top:218px;width:94px;height:76px}
  .natural-badge path,.natural-badge polygon{fill:none;stroke:var(--logo)}
  .brand-est{
    position:absolute;top:279px;left:20px;width:136px;display:flex;justify-content:space-between;
    font-size:8.5px;font-weight:500;color:var(--ink);
  }
  .brand-est__est{font-family:"Josefin Sans",sans-serif;letter-spacing:4px}
</style>
</head>
<body>

<!-- SLEEP -->
<article class="label label--sleep">
  <div class="label__art" role="img" aria-label="Etched organic texture in deep blue tones"></div>
  <div class="label__seal" role="img" aria-label="Money back guarantee seal"></div>
  <div class="label__info">
    <p class="est-line"><span class="est-line__est">EST.</span><span class="est-line__name">VERDANE</span><span class="est-line__year">10,000 BC</span></p>
    <h2 class="label__title">SLEEP</h2>
    <p class="dose">
      <svg class="dose__pill" viewBox="0 0 22 14"><ellipse cx="11" cy="7" rx="10" ry="6" fill="none" stroke="currentColor" stroke-width="1.6"/><line x1="1" y1="7" x2="21" y2="7" stroke="currentColor" stroke-width="1.4"/></svg>
      <span class="dose__count">×30</span><span class="dose__kind">SUPPLEMENT</span><span class="dose__mg">1125mg</span>
    </p>
    <span class="rule rule--1"></span>
    <p class="copy copy--purpose"><strong>VERDANE’S PURPOSE</strong> is to support health, wellbeing and longevity, so that we can all thrive in the modern world; an environment so alien to that in which we evolved. Embracing technology, research and science, we harness nature’s goodness - enabling us all to love life – naturally.</p>
    <span class="rule rule--2"></span>
    <p class="copy copy--pledge"><strong>TWICE EACH DAY PLEDGE:</strong> For each and every Verdane supplement you take, we provide a supplement to an under nourished child.</p>
    <span class="rule rule--3"></span>
  </div>
  <div class="label__brand">
    <p class="brand-name">VERDANE<br>WAY</p>
    <p class="brand-tagline">Thriving Days Outdoors</p>
    <svg class="natural-badge" viewBox="0 0 94 76" role="img" aria-label="Natural product badge"><polygon points="47,8 86,38 47,68 8,38" stroke-width="1.6"/><polygon points="47,14 79,38 47,62 15,38" stroke-width="0.8"/></svg>
    <p class="brand-est"><span class="brand-est__est">EST.</span><span>10,000 BC</span></p>
  </div>
</article>

<!-- GREEN TEA -->
<article class="label label--tea">
  <div class="label__art" role="img" aria-label="Etched organic texture in deep green tones"></div>
  <div class="label__seal" role="img" aria-label="Money back guarantee seal"></div>
  <div class="label__info">
    <p class="est-line"><span class="est-line__est">EST.</span><span class="est-line__name">VERDANE</span><span class="est-line__year">10,000 BC</span></p>
    <h2 class="label__title">GREEN TEA</h2>
    <p class="dose">
      <svg class="dose__pill" viewBox="0 0 22 14"><ellipse cx="11" cy="7" rx="10" ry="6" fill="none" stroke="currentColor" stroke-width="1.6"/><line x1="1" y1="7" x2="21" y2="7" stroke="currentColor" stroke-width="1.4"/></svg>
      <span class="dose__count">×30</span><span class="dose__kind dose__kind--wide">EXTRACT</span><span class="dose__mg">1125mg</span>
    </p>
    <span class="rule rule--1"></span>
    <p class="copy copy--purpose"><strong>VERDANE’S PURPOSE</strong> is to support health, wellbeing and longevity, so that we can all thrive in the modern world; an environment so alien to that in which we evolved. Embracing technology, research and science, we harness nature’s goodness - enabling us all to love life – naturally.</p>
    <span class="rule rule--2"></span>
    <p class="copy copy--pledge"><strong>TWICE EACH DAY PLEDGE:</strong> For each and every Verdane supplement you take, we provide a supplement to an under nourished child.</p>
    <span class="rule rule--3"></span>
  </div>
  <div class="label__brand">
    <p class="brand-name">VERDANE<br>WAY</p>
    <p class="brand-tagline">Thriving Days Outdoors</p>
    <svg class="natural-badge" viewBox="0 0 94 76" role="img" aria-label="Natural product badge"><polygon points="47,8 86,38 47,68 8,38" stroke-width="1.6"/><polygon points="47,14 79,38 47,62 15,38" stroke-width="0.8"/></svg>
    <p class="brand-est"><span class="brand-est__est">EST.</span><span>10,000 BC</span></p>
  </div>
</article>

<!-- ENERGY -->
<article class="label label--energy">
  <div class="label__art" role="img" aria-label="Etched organic texture in deep red tones"></div>
  <div class="label__seal" role="img" aria-label="Money back guarantee seal"></div>
  <div class="label__info">
    <p class="est-line"><span class="est-line__est">EST.</span><span class="est-line__name">VERDANE</span><span class="est-line__year">10,000 BC</span></p>
    <h2 class="label__title">ENERGY</h2>
    <p class="dose">
      <svg class="dose__pill" viewBox="0 0 22 14"><ellipse cx="11" cy="7" rx="10" ry="6" fill="none" stroke="currentColor" stroke-width="1.6"/><line x1="1" y1="7" x2="21" y2="7" stroke="currentColor" stroke-width="1.4"/></svg>
      <span class="dose__count">×30</span><span class="dose__kind">SUPPLEMENT</span><span class="dose__mg">1125mg</span>
    </p>
    <span class="rule rule--1"></span>
    <p class="copy copy--purpose"><strong>VERDANE’S PURPOSE</strong> is to support health, wellbeing and longevity, so that we can all thrive in the modern world; an environment so alien to that in which we evolved. Embracing technology, research and science, we harness nature’s goodness - enabling us all to love life – naturally.</p>
    <span class="rule rule--2"></span>
    <p class="copy copy--pledge"><strong>TWICE EACH DAY PLEDGE:</strong> For each and every Verdane supplement you take, we provide a supplement to an under nourished child.</p>
    <span class="rule rule--3"></span>
  </div>
  <div class="label__brand">
    <p class="brand-name">VERDANE<br>WAY</p>
    <p class="brand-tagline">Thriving Days Outdoors</p>
    <svg class="natural-badge" viewBox="0 0 94 76" role="img" aria-label="Natural product badge"><polygon points="47,8 86,38 47,68 8,38" stroke-width="1.6"/><polygon points="47,14 79,38 47,62 15,38" stroke-width="0.8"/></svg>
    <p class="brand-est"><span class="brand-est__est">EST.</span><span>10,000 BC</span></p>
  </div>
</article>

<!-- VITAMIN D3 -->
<article class="label label--d3">
  <div class="label__art" role="img" aria-label="Etched organic texture in amber and brown tones"></div>
  <div class="label__seal" role="img" aria-label="Money back guarantee seal"></div>
  <div class="label__info">
    <p class="est-line"><span class="est-line__est">EST.</span><span class="est-line__name">VERDANE</span><span class="est-line__year">10,000 BC</span></p>
    <h2 class="label__title">VITAMIN D<sup>3</sup></h2>
    <p class="dose">
      <svg class="dose__pill" viewBox="0 0 22 14"><ellipse cx="11" cy="7" rx="10" ry="6" fill="none" stroke="currentColor" stroke-width="1.6"/><line x1="1" y1="7" x2="21" y2="7" stroke="currentColor" stroke-width="1.4"/></svg>
      <span class="dose__count">×30</span><span class="dose__kind">SUPPLEMENT</span><span class="dose__mg">1125mg</span>
    </p>
    <span class="rule rule--1"></span>
    <p class="copy copy--purpose"><strong>VERDANE’S PURPOSE</strong> is to support health, wellbeing and longevity, so that we can all thrive in the modern world; an environment so alien to that in which we evolved. Embracing technology, research and science, we harness nature’s goodness - enabling us all to love life – naturally.</p>
    <span class="rule rule--2"></span>
    <p class="copy copy--pledge"><strong>TWICE EACH DAY PLEDGE:</strong> For each and every Verdane supplement you take, we provide a supplement to an under nourished child.</p>
    <span class="rule rule--3"></span>
  </div>
  <div class="label__brand">
    <p class="brand-name">VERDANE<br>WAY</p>
    <p class="brand-tagline">Thriving Days Outdoors</p>
    <svg class="natural-badge" viewBox="0 0 94 76" role="img" aria-label="Natural product badge"><polygon points="47,8 86,38 47,68 8,38" stroke-width="1.6"/><polygon points="47,14 79,38 47,62 15,38" stroke-width="0.8"/></svg>
    <p class="brand-est"><span class="brand-est__est">EST.</span><span>10,000 BC</span></p>
  </div>
</article>

</body>
</html>
```